KORVELTA Corporate Business Card

Modern business card design for company which focuses in the areas of Staffing, IT Consulting & Data Services. Please note: We are no longer using the IT subscript on the logo. All designs should have IT subscript removed.
Website: www.korveltait.example

```html
<!DOCTYPE html>
<html lang="en">
<head>
<meta charset="utf-8">
<title>KORVELTA Business Card</title>
<link rel="stylesheet" href="https://fonts.googleapis.com/css2?family=Montserrat:wght@400;500;700&display=swap">
<style>
  :root {
    --backdrop: #151515;
    --card: #262626;
    --card-edge: #2f2f2f;
    --brand-blue: #1f9ae0;
    --text-light: #f2f2f2;
  }
  * { margin: 0; padding: 0; box-sizing: border-box; }
  html, body {
    width: 1200px; height: 900px; overflow: hidden;
    background: var(--backdrop);
    font-family: "Montserrat", sans-serif;
  }
  .canvas {
    position: relative; width: 1200px; height: 900px;
    display: flex; flex-direction: column; align-items: center; justify-content: center; gap: 40px;
  }
  .card {
    position: relative; width: 700px; height: 400px;
    background: linear-gradient(135deg, var(--card) 0%, var(--card) 60%, var(--card-edge) 100%);
    box-shadow: 0 12px 30px rgba(0,0,0,0.6);
  }
  .wordmark {
    display: flex; align-items: center; gap: 12px;
    color: var(--brand-blue); font-weight: 700; letter-spacing: 2px;
  }
  .wordmark-square {
    display: block; background: var(--brand-blue); border-radius: 4px;
  }
  .card-front { display: flex; align-items: center; justify-content: center; }
  .card-front .wordmark { font-size: 64px; }
  .card-front .wordmark-square { width: 46px; height: 46px; }

  .card-back { display: flex; align-items: center; }
  .card-back .brand-side {
    width: 340px; display: flex; justify-content: center;
  }
  .card-back .wordmark { font-size: 40px; gap: 10px; }
  .card-back .wordmark-square { width: 30px; height: 30px; }
  .divider {
    width: 2px; height: 200px; background: var(--brand-blue);
  }
  .details { padding-left: 40px; color: var(--text-light); }
  .person-name {
    color: var(--brand-blue); font-size: 28px; font-weight: 500; letter-spacing: 2px;
    text-transform: uppercase; line-height: 1.1;
  }
  .person-role { font-size: 18px; margin-bottom: 18px; }
  .address { font-size: 18px; line-height: 1.3; margin-bottom: 10px; }
  .contact-line { display: flex; align-items: center; gap: 10px; font-size: 18px; line-height: 1.45; }
  .contact-line svg { width: 14px; height: 14px; flex: none; }
</style>
</head>
<body>
<main class="canvas">
  <section class="card card-front">
    <div class="wordmark"><span class="wordmark-square"></span>KORVELTA</div>
  </section>

  <section class="card card-back">
    <div class="brand-side">
      <div class="wordmark"><span class="wordmark-square"></span>KORVELTA</div>
    </div>
    <div class="divider"></div>
    <div class="details">
      <p class="person-name">Daniel Hartley</p>
      <p class="person-role">Director</p>
      <p class="address">418 Larchmont Ave.<br>Brookfield, OH 44403</p>
      <p class="contact-line">
        <svg viewBox="0 0 16 16"><path d="M4 1.5l2.5 3-1.5 1.5c.8 1.8 2.2 3.2 4 4l1.5-1.5 3 2.5-1.5 2.5C7 13.5 2.5 9 1.5 3.5z" fill="none" stroke="var(--brand-blue)" stroke-width="1.4"/></svg>
        555-014-7720
      </p>
      <p class="contact-line">
        <svg viewBox="0 0 16 16"><rect x="1.5" y="3.5" width="13" height="9" fill="none" stroke="var(--brand-blue)" stroke-width="1.4"/><path d="M1.5 3.5l6.5 5 6.5-5" fill="none" stroke="var(--brand-blue)" stroke-width="1.4"/></svg>
        contactus@korveltait.example
      </p>
      <p class="contact-line">
        <svg viewBox="0 0 16 16"><circle cx="8" cy="8" r="6.5" fill="none" stroke="var(--brand-blue)" stroke-width="1.3"/><ellipse cx="8" cy="8" rx="2.8" ry="6.5" fill="none" stroke="var(--brand-blue)" stroke-width="1.1"/><path d="M1.5 8h13" stroke="var(--brand-blue)" stroke-width="1.1"/></svg>
        www.korveltait.example
      </p>
    </div>
  </section>
</main>
</body>
</html>
```